Store Signage for New Location

I need a banner for my new location. It needs to communicate 1: our name, 2: our phone number 3: our message. This is going to be a 7 foot wide banner that is 4 feet tall. It needs to be a very high resolution design so it prints properly.

Our phone number is (555) 418-2097

Our Message: The HONEST alternative to the dealer.

Or: Your Honest Auto Service Center

"Honest" is our key word here.
Updates

Target Market(s)

Drive-by traffic.

Industry/Entity Type

Auto Repair

Requirements
Must have
• The name of our business: Fair Lane Auto Repair
• Our phone number: (555) 418-2097
• Our message: The HONEST alternative to the dealership.
• or: Your Honest Service Center
Nice to have
• I really just need a clean layout using the uploaded logo and font. It needs to be highly visible as a sign that is seen by drive-by traffic.
• I'd like the color scheme to be the same as what I have, however, you're more than welcome to add detail and color as needed.

```html
<!DOCTYPE html>
<html lang="en">
<head>
<meta charset="utf-8">
<title>Fair Lane Auto Repair – Store Banner</title>
<link rel="stylesheet" href="https://fonts.googleapis.com/css2?family=Exo+2:ital,wght@0,700;1,700;1,800;1,900&family=Oswald:wght@500;600&display=swap">
<style>
  :root {
    --page-bg: #3c3c3d;
    --orange: #ef8418;
    --orange-light: #f59a35;
    --charcoal: #24272c;
    --charcoal-soft: #2e3238;
    --white: #ffffff;
    --accent-red: #e2461d;
    --photo-dark: #4a4548;
    --photo-mid: #8a7f80;
    --photo-light: #c9c2be;
  }
  * { margin: 0; padding: 0; box-sizing: border-box; }
  html, body {
    width: 846px; height: 1200px; overflow: hidden;
    background: var(--page-bg);
  }
  .banner {
    position: absolute;
    left: 33px; top: 377px;
    width: 682px; height: 390px;
    transform: scale(1.1437);
    transform-origin: 0 0;
    overflow: hidden;
    font-family: "Exo 2", sans-serif;
  }
  .banner__shapes { position: absolute; inset: 0; }
  .brand {
    position: absolute; left: 20px; top: 26px;
    display: flex; align-items: center; gap: 8px;
  }
  .brand__dot { width: 16px; height: 16px; border-radius: 50%; background: var(--accent-red); }
  .brand__name { font-weight: 700; font-size: 15px; color: var(--white); letter-spacing: .2px; }
  .headline { position: absolute; inset: 0; pointer-events: none; }
  .headline span {
    position: absolute; font-style: italic; font-weight: 900;
    line-height: 1; white-space: nowrap;
    text-shadow: 2px 2px 0 rgba(36,39,44,.55);
  }
  .headline__honest { left: 334px; top: 22px; font-size: 38px; color: var(--white); }
  .headline__alternative { left: 366px; top: 62px; font-size: 38px; color: var(--charcoal); text-shadow: 1px 1px 0 rgba(255,255,255,.25); }
  .headline__tothe { left: 382px; top: 115px; font-size: 11px; font-weight: 800; color: var(--white); text-shadow: none; }
  .headline__dealership { left: 428px; top: 99px; font-size: 38px; color: var(--white); }
  .services-title {
    position: absolute; left: 402px; top: 152px; width: 280px; height: 34px;
    display: flex; align-items: center; justify-content: center;
    font-style: italic; font-weight: 800; font-size: 22px; color: var(--white);
  }
  .service {
    position: absolute; font-style: italic; font-weight: 700;
    font-size: 10.5px; line-height: 1.15; color: var(--charcoal);
    white-space: nowrap;
  }
  .phone {
    position: absolute; left: 14px; top: 332px;
    font-family: "Oswald", sans-serif; font-weight: 500;
    font-size: 31px; color: var(--white); letter-spacing: .5px;
    white-space: nowrap;
  }
  .address {
    position: absolute; left: 366px; top: 358px;
    font-family: "Oswald", sans-serif; font-weight: 500;
    font-size: 16px; color: var(--white); letter-spacing: .3px;
    white-space: nowrap;
  }
</style>
</head>
<body>
<main class="banner">
  <svg class="banner__shapes" viewBox="0 0 682 390" width="682" height="390">
    <defs>
      <linearGradient id="photo-tone" x1="0" y1="0" x2="1" y2="1">
        <stop offset="0" stop-color="var(--photo-light)"/>
        <stop offset=".45" stop-color="var(--photo-mid)"/>
        <stop offset="1" stop-color="var(--photo-dark)"/>
      </linearGradient>
      <radialGradient id="inset-tone" cx=".4" cy=".4" r=".7">
        <stop offset="0" stop-color="#e8e6e4"/>
        <stop offset=".6" stop-color="#6e6a6b"/>
        <stop offset="1" stop-color="#2b2a2c"/>
      </radialGradient>
    </defs>

    <rect class="field-orange" width="682" height="390" fill="var(--orange)"/>
    <path d="M560 0 Q640 60 600 150" stroke="var(--orange-light)" stroke-width="26" fill="none" opacity=".45"/>

    <polygon class="panel-dark" points="0,0 262,0 418,192 286,390 0,390" fill="var(--charcoal)"/>

    <polygon class="photo-area" role="img" aria-label="Photo of a mechanic mounting a wheel and tyre on a car in a workshop"
      points="0,75 258,75 356,192 272,322 0,322" fill="url(#photo-tone)"/>

    <polygon class="chevron-stripe" points="228,0 246,0 402,192 268,390 250,390 384,192" fill="var(--white)"/>
    <polygon class="chevron-stripe" points="284,0 292,0 452,192 316,390 308,390 444,192" fill="var(--charcoal)" opacity=".9"/>

    <rect class="band-services" x="402" y="152" width="280" height="34" fill="var(--charcoal)"/>

    <polygon class="band-address" points="338,352 682,352 682,390 314,390" fill="var(--charcoal)"/>

    <circle cx="384" cy="262" r="56" fill="none" stroke="var(--white)" stroke-width="1" opacity=".7"/>
    <circle class="photo-inset" role="img" aria-label="Close-up photo of gloved hands checking an engine with a clipboard"
      cx="384" cy="262" r="51" fill="url(#inset-tone)"/>

    <g class="service-icons" fill="var(--white)">
      <polygon points="438,202 454,211 454,229 438,238 422,229 422,211"/>
      <polygon points="578,202 594,211 594,229 578,238 562,229 562,211"/>
      <polygon points="438,252 454,261 454,279 438,288 422,279 422,261"/>
      <polygon points="578,252 594,261 594,279 578,288 562,279 562,261"/>
      <polygon points="438,302 454,311 454,329 438,338 422,329 422,311"/>
      <polygon points="578,302 594,311 594,329 578,338 562,329 562,311"/>
    </g>
    <g class="service-glyphs" fill="none" stroke="var(--charcoal)" stroke-width="1.6">
      <circle cx="438" cy="220" r="8"/><circle cx="438" cy="220" r="3"/>
      <circle cx="578" cy="220" r="8.5" stroke-width="2.4"/><circle cx="578" cy="220" r="3.5"/>
      <path d="M428 274 L430 266 H446 L448 274 Z" fill="var(--charcoal)"/>
      <circle cx="432" cy="276" r="2" fill="var(--charcoal)"/><circle cx="444" cy="276" r="2" fill="var(--charcoal)"/>
      <path d="M570 265 H584 V277 H570 Z"/><path d="M584 268 L590 264"/><path d="M588 272 q2 3 0 4 q-2 -1 0 -4" fill="var(--charcoal)"/>
      <rect x="431" y="310" width="14" height="18" rx="1"/><path d="M435 316 h6 M435 320 h6 M435 324 h6"/>
      <path d="M569 315 H583 V318 H588 V326 H583 V328 H571 L569 325 H566 V318 H569 Z" fill="var(--charcoal)"/>
    </g>

    <path class="icon-pin" d="M345 362 a6 6 0 0 1 12 0 c0 5 -6 11 -6 11 c0 0 -6 -6 -6 -11 Z M347 376 h8"
      fill="none" stroke="var(--white)" stroke-width="1.5"/>
  </svg>

  <div class="brand">
    <span class="brand__dot"></span>
    <span class="brand__name">Fair Lane Auto Repair</span>
  </div>

  <h1 class="headline">
    <span class="headline__honest">THE HONEST</span>
    <span class="headline__alternative">ALTERNATIVE</span>
    <span class="headline__tothe">TO THE</span>
    <span class="headline__dealership">DEALERSHIP</span>
  </h1>

  <h2 class="services-title">What we do?</h2>

  <p class="service" style="left:461px;top:214px;">Brake Repair</p>
  <p class="service" style="left:601px;top:214px;">Tires</p>
  <p class="service" style="left:461px;top:264px;">Fleet Services</p>
  <p class="service" style="left:601px;top:264px;">Oil Change</p>
  <p class="service" style="left:461px;top:308px;">Factory Scheduled<br>Maintenance</p>
  <p class="service" style="left:601px;top:308px;">Check Engine<br>Light</p>

  <p class="phone">(555) 418-2097</p>
  <p class="address">4270 W, 58TH STREET, LAKEVIEW, KS 66100</p>
</main>
</body>
</html>
```